Best Selling Book Cover Design for Non-Fiction Adventure

Hello there!I'm looking for a gorgeous front and back book cover design worthy of a Best Seller for my book that will be published next week. It is about the story of my walk of the Sendero de Valdoria, the 500-mile pilgrimage across the northern part of Spain. I've attached a detailed description along with the content for the back cover. I'm also attaching a bunch of pictures from the walk although it is not necessary to any of these. I need a cover that sells and speaks to the description, whatever you think that will be best. Book DetailsTitle: One Million StepsSubtitle: Lessons From A Legendary HikeAuthor: Ngan H. NguyenSpecifics:- The book will be 5.5" by 8.5" and 194 pages (may change slightly and we can update the spine in final revisions). - Paperback and leave space for a bar code- Will need the raw files so this can be redesigned into hardcover down the line- Brindlemart book cover upload ready- Final file will also need the front cover only for e-book version- Add profile headshot (attached) to back-cover if space permits.

Target Market(s)

Those interested in adventure stories, spirituality, healing, transformation, self-actualization.

Font styles to use
Serif
Script

Colors

Designer to choose colors to be used in the design.

Requirements
Nice to have
• Potentially some of the infamous symbols of the Sendero like the seashell or yellow arrows. Maybe fog or mist over the path or village to create a mysterious feel. Not all mandatory.
• Maybe some cool blending effects of various artifacts or pictures.

```html
<!DOCTYPE html>
<html lang="en">
<head>
<meta charset="utf-8">
<title>Beneath the Far Ridge – Cover Spread</title>
<link rel="stylesheet" href="https://fonts.googleapis.com/css2?family=Cinzel:wght@700;900&family=Quicksand:wght@500;600;700&display=swap">
<style>
  :root {
    --page: #ffffff;
    --night: #0f1f5c;
    --night-deep: #0a1340;
    --sky-mid: #1d3f8f;
    --hill: #5aa63a;
    --hill-light: #8fcf4a;
    --road: #7fc6d6;
    --panel: rgba(28, 58, 160, 0.62);
    --panel-bio: rgba(30, 52, 130, 0.6);
    --text-light: #ffffff;
    --text-dark: #0d1630;
    --gold-1: #fff1a8;
    --gold-2: #e6b53a;
    --gold-3: #9c6410;
    --shell: #b89a4e;
    --shell-dark: #6e5622;
  }
  * { box-sizing: border-box; margin: 0; padding: 0; }
  html, body { width: 1200px; height: 1200px; overflow: hidden; background: var(--page); }
  .canvas { position: relative; width: 1200px; height: 1200px; background: var(--page); }

  .spread {
    position: absolute; left: 41px; top: 185px; width: 1120px; height: 832px; overflow: hidden;
  }
  .spread-art {
    position: absolute; inset: 0;
    background:
      radial-gradient(ellipse 40% 35% at 88% 10%, rgba(70,120,40,0.9), transparent 70%),
      radial-gradient(ellipse 60% 30% at 70% 98%, var(--road), transparent 70%),
      linear-gradient(180deg, var(--night-deep) 0%, var(--night) 25%, var(--sky-mid) 50%, var(--hill) 72%, var(--hill-light) 88%, #4f9a3a 100%);
  }

  .back-blurb {
    position: absolute; left: 38px; top: 45px; width: 474px; height: 494px;
    background: var(--panel); color: var(--text-light);
    font-family: 'Quicksand', sans-serif; font-weight: 600;
    font-size: 13px; line-height: 16.4px; text-align: center;
    padding: 24px 14px 0;
  }
  .back-blurb h2 { font-size: 12.5px; font-weight: 700; letter-spacing: 0.3px; margin-bottom: 15px; }
  .back-blurb p { margin-bottom: 16px; }

  .author-bio {
    position: absolute; left: 41px; top: 557px; width: 247px; height: 251px;
    background: var(--panel-bio); color: var(--text-light);
    font-family: 'Quicksand', sans-serif; font-weight: 500;
    font-size: 10.4px; line-height: 13.1px; padding: 51px 13px 0;
  }
  .author-photo {
    position: absolute; left: 317px; top: 551px; width: 120px; height: 119px;
    border: 2px solid #fff; background: linear-gradient(160deg, #3a3f4a, #6b5a52 60%, #2a2a30);
  }
  .barcode-space { position: absolute; left: 317px; top: 689px; width: 196px; height: 118px; background: #fff; }

  .spine-text {
    position: absolute; left: 548px; top: 59px; width: 30px; height: 730px;
    writing-mode: vertical-rl; color: var(--text-light);
    font-family: 'Quicksand', sans-serif; font-weight: 700; font-size: 15.5px; letter-spacing: 0.6px;
    display: flex; align-items: center; gap: 26px;
  }
  .spine-title { letter-spacing: 1.6px; }

  .front-author {
    position: absolute; left: 717px; top: 50px; width: 260px; text-align: center;
    font-family: 'Quicksand', sans-serif; font-weight: 700; font-size: 29px; letter-spacing: 2.5px;
    color: var(--text-light);
  }
  .front-title { position: absolute; left: 607px; top: 170px; width: 480px; height: 200px; }
  .front-title text { font-family: 'Cinzel', serif; font-weight: 900; }
  .shell-emblem {
    position: absolute; left: 907px; top: 539px; width: 180px; height: 220px;
    background: radial-gradient(ellipse at 50% 40%, #e0c77a, var(--shell) 55%, var(--shell-dark));
  }
  .front-subtitle {
    position: absolute; left: 635px; top: 770px; width: 430px; text-align: center;
    font-family: 'Quicksand', sans-serif; font-weight: 700; font-size: 23px; letter-spacing: 1.6px;
    color: var(--text-dark); white-space: nowrap;
  }
</style>
</head>
<body>
<div class="canvas">
  <section class="spread">
    <div class="spread-art" role="img" aria-label="Painted night landscape: starry blue sky, a leafy tree at top right, green rolling hills and a winding pale road running down the front cover"></div>

    <div class="back-blurb">
      <h2>BENEATH THE FAR RIDGE: TALES GATHERED ON A QUIET ROAD</h2>
      <p>Stretching 500-miles across the northern part of Spain is the Sendero Francés of the Sendero de Valdoria. A pilgrimage to the Spanish city of Valdoria de Compostela.</p>
      <p>It was by fate that I found this path and it became one of the greatest adventures of my life. Over a million steps crossing the rugged Pyrenees and spanning undulating plains before winding through lush hillsides. The path was a unique window into historical, natural and cultural beauty, but even more than that, it was a walk into more depth within my own being. It became a journey of healing and self-discovery.</p>
      <p>The many gifts, lessons, and miracles that I came to discover along this path allowed me to see how the path mirrors our journey to any destination we have in mind. Arriving at Valdoria de Compostela, I was transformed and the gifts the path brought me was more than I ever thought was possible.</p>
      <p>In this book, I tell the story of that adventure as well as the countless powerful lessons I learned in the hope that it may of service to you. May the lessons I learned shine more light on your journey to whatever destination that may be pulling at your consciousness at this moment.</p>
      <p>Buen Sendero – Good Way to You.</p>
    </div>

    <div class="author-bio">Thao K. Pham has built her platform of a vision-driven life after 10 years of experience working as a business strategy advisor in Top 500 companies and at Harlow &amp; Reed. Combining her advisory experience with her passion for spiritual principles of success, she now empowers entrepreneurs, change-makers, and leaders to step into their truth and bring their unique vision to life. Enabling them to change their lives, revolutionize their work, create greater impact in the world.</div>
    <div class="author-photo" role="img" aria-label="Author headshot"></div>
    <div class="barcode-space"></div>

    <div class="spine-text">
      <span class="spine-title">BENEATH THE FAR RIDGE</span>
      <span>Tales Gathered On A Quiet Road</span>
      <span>Thao K. Pham</span>
    </div>

    <div class="front-author">Thao K. Pham</div>
    <svg class="front-title" viewBox="0 0 480 200" aria-label="Beneath the Far Ridge">
      <defs>
        <linearGradient id="gold" x1="0" y1="0" x2="0" y2="1">
          <stop offset="0" stop-color="var(--gold-1)"/>
          <stop offset="0.5" stop-color="var(--gold-2)"/>
          <stop offset="1" stop-color="var(--gold-3)"/>
        </linearGradient>
      </defs>
      <text x="240" y="58" text-anchor="middle" font-size="58" textLength="440" lengthAdjust="spacingAndGlyphs" fill="url(#gold)" stroke="#5a3408" stroke-width="1.5">BENEATH THE</text>
      <text x="240" y="182" text-anchor="middle" font-size="112" textLength="480" lengthAdjust="spacingAndGlyphs" fill="url(#gold)" stroke="#5a3408" stroke-width="2">FAR RIDGE</text>
    </svg>
    <div class="shell-emblem" role="img" aria-label="Carved golden scallop shell emblem on a stone tile"></div>
    <div class="front-subtitle">Tales Gathered On A Quiet Road</div>
  </section>
</div>
</body>
</html>
```